Business Card Design needed for start up company Pramora

In need of a new business card designed for a start up company based in Sydney, Pramora is a new start up innovative Company, our mission it to make property accessible for everyday Australian and to become the leading Real Estate platform in Australia. We want it to be fresh and clean.

Industry/Entity Type

Financial

Contact Information for Business Card

Section for Name
Section for Title

PRAMORA - Where Doors Open Wide
Mobile:
Direct:

Font styles to use
Sans Serif

Colors
33a6d7
0692cd
0255a3
ffffff

Requirements
Must have
• Logo, all business card details

```html
<!DOCTYPE html>
<html lang="en">
<head>
<meta charset="utf-8">
<title>Pramora Business Card</title>
<link rel="stylesheet" href="https://fonts.googleapis.com/css2?family=Source+Sans+3:wght@400;600&display=swap">
<style>
  :root {
    --page-bg: #d9dcdf;
    --card-light: #f3f5f6;
    --card-mid: #e6eaed;
    --blue-light: #33a6d7;
    --blue-mid: #0692cd;
    --blue-deep: #0255a3;
    --white: #ffffff;
    --text-soft: #e3f1fa;
  }
  html, body {
    margin: 0;
    width: 1200px;
    height: 969px;
    overflow: hidden;
    background: var(--page-bg);
    font-family: "Source Sans 3", Arial, sans-serif;
  }
  .card {
    position: absolute;
    left: 100px;
    top: 199px;
    width: 1000px;
    height: 571px;
    background: linear-gradient(135deg, var(--card-light), var(--card-mid));
    box-shadow: 0 10px 30px rgba(0,0,0,0.18);
    overflow: hidden;
  }
  .card-band {
    position: absolute;
    inset: 0;
    width: 1000px;
    height: 571px;
  }
  .brand-name {
    position: absolute;
    left: 70px;
    top: 104px;
    font-size: 66px;
    font-weight: 600;
    letter-spacing: 2px;
    color: var(--blue-deep);
    line-height: 1;
  }
  .details {
    position: absolute;
    right: 40px;
    top: 206px;
    text-align: right;
    color: var(--text-soft);
  }
  .person-name {
    font-size: 30px;
    font-weight: 600;
    color: var(--white);
    letter-spacing: 0.5px;
    line-height: 36px;
  }
  .person-title {
    font-size: 25px;
    line-height: 32px;
    margin-bottom: 22px;
  }
  .address { margin-bottom: 8px; }
  .address-line {
    font-size: 23px;
    line-height: 33px;
  }
  .contact-line {
    font-size: 23px;
    line-height: 32px;
    display: flex;
    justify-content: flex-end;
    align-items: center;
    gap: 14px;
  }
  .contact-icon {
    width: 20px;
    height: 20px;
    fill: var(--text-soft);
  }
  .tagline {
    font-size: 23px;
    line-height: 34px;
  }
</style>
</head>
<body>
  <div class="card">
    <svg class="card-band" viewBox="0 0 1000 571" aria-hidden="true">
      <defs>
        <linearGradient id="bandFill" x1="0" y1="1" x2="1" y2="0">
          <stop offset="0" stop-color="#0692cd"/>
          <stop offset="1" stop-color="#0255a3"/>
        </linearGradient>
      </defs>
      <path d="M0,571 L0,500 C300,480 480,160 1000,120 L1000,571 Z" fill="url(#bandFill)"/>
    </svg>

    <div class="brand-name">PRAMORA</div>

    <div class="details">
      <div class="person-name">LIAM CARTER</div>
      <div class="person-title">CEO/FOUNDER</div>
      <div class="address">
        <div class="address-line">42 Harbour Street</div>
        <div class="address-line">Sydney, NSW 2000</div>
      </div>
      <div class="contact-line">02 5550 1934
        <svg class="contact-icon" viewBox="0 0 20 20"><path d="M2 7c0-3 3-4 8-4s8 1 8 4l-3 1-1-2H6L5 8zM5 9h10l2 8H3z"/></svg>
      </div>
      <div class="contact-line">0412 555 018
        <svg class="contact-icon" viewBox="0 0 20 20"><path d="M6 1h8a1 1 0 0 1 1 1v16a1 1 0 0 1-1 1H6a1 1 0 0 1-1-1V2a1 1 0 0 1 1-1zm1 2v12h6V3z"/></svg>
      </div>
      <div class="contact-line">liam@pramora.com.au
        <svg class="contact-icon" viewBox="0 0 20 20"><path d="M2 5h16v10H2zm1 1 7 5 7-5z" fill-rule="evenodd"/></svg>
      </div>
      <div class="contact-line">www.pramora.com.au
        <svg class="contact-icon" viewBox="0 0 20 20"><circle cx="10" cy="10" r="8"/><path d="M4 8h12M4 12h12M10 2c-3 4-3 12 0 16M10 2c3 4 3 12 0 16" stroke="#0255a3" stroke-width="1.2" fill="none"/></svg>
      </div>
      <div class="tagline">Where Doors Open Wide</div>
    </div>
  </div>
</body>
</html>
```